Flyer Design

i would like a double sided two different treatments colour scheme is red and white first side….
brightline grins (teeth whitening )

we use a non peroxide gel so no sensitivity at all and completely pain free cosmetic procedure.
we offer two different treatments…
20 minute express £30 each or 2 people for £50
45 minute premium (longer lasting) £50 each or 2 people for £80
i also do gift certificates perfect for birthdays christmas or just the one you love
i would like a voucher added on here if they bring the voucher they can claim a free top up pen or have an extra 10% off
i would like my details on here
name rebecca dowd
number 01632960418
address 27 heol y felin pentwyn cf145qt
email dowdkevindowd@mailbox-example.co.uk

other side…. again colours in red and white
velvetwave laser lipo
A non-invasive treatment that every salon and spa must have! Say no to Liposuction, surgery or crash diet. This new innovative laser technology will break down the fat cells and promote the triglyceride in the cells overflow. The fat cells are significantly reduced, achieving weight loss immediately. At the same time, the outflow of the glycerol and free acids are decomposed in part by capillaries and lymphatic microtubule, partly transformed into energy by movement, and partly excreted by the kidneys. The velvetwave laser lipo can reduce from 2-15cm of body fat after a single treatment. The procedure is fast, relaxing and effective on any body parts without causing any side effects to the client.

cost is £40 per session or full course of 8 sessions at £199
i also do gift certificates perfect for birthdays, christmas or just the one you love.
also a voucher with an extra 10% off

name: rebecca dowd
number: 01632 960418
address: 27 heol y felin pentwyn cf145qt
email address: dowdkevindowd@mailbox-example.co.uk

Weight

```html
<!DOCTYPE html>
<html lang="en">
<head>
<meta charset="utf-8">
<title>Velvetwave Laser Lipo &amp; Brightline Grins Flyers</title>
<link rel="stylesheet" href="https://fonts.googleapis.com/css2?family=Open+Sans:wght@400;600;700;800&family=Roboto+Condensed:ital,wght@0,400;1,300;1,400;1,700&display=swap">
<style>
  :root {
    --red: #e2401f;
    --deep-red: #b8231a;
    --banner-red: #d83a1f;
    --shadow-black: #1c1c1c;
    --ink: #111111;
    --paper: #ffffff;
    --stage: #2a2a2a;
  }
  * { margin: 0; padding: 0; box-sizing: border-box; }
  html, body { width: 1200px; height: 1122px; overflow: hidden; background: var(--stage); }
  .canvas { position: relative; width: 1200px; height: 1122px; }

  .flyer {
    position: absolute;
    background: var(--paper);
    overflow: hidden;
    transform-origin: top left;
    transform: scale(0.9685);
    font-family: "Open Sans", sans-serif;
    color: var(--ink);
  }
  .flyer--lipo { left: 39px; top: 69px; width: 666px; height: 470px; }
  .flyer--whitening { left: 416px; top: 559px; width: 730px; height: 497px; }

  .wash {
    position: absolute; left: 0; right: 0; bottom: 0;
    background: linear-gradient(100deg, rgba(246,140,70,0.55) 0%, rgba(255,220,190,0.35) 40%, rgba(255,255,255,0) 60%, rgba(159,203,232,0.6) 100%);
  }
  .flyer--lipo .wash { top: 285px; -webkit-mask-image: linear-gradient(to bottom, transparent, #000 35%); mask-image: linear-gradient(to bottom, transparent, #000 35%); }
  .flyer--whitening .wash { top: 300px; left: 280px; -webkit-mask-image: linear-gradient(to bottom, transparent, #000 40%); mask-image: linear-gradient(to bottom, transparent, #000 40%); }

  .art { position: absolute; left: 0; top: 0; }

  .headline-text { font-family: "Roboto Condensed", sans-serif; font-weight: 400; fill: var(--paper); }
  .headline-phone { font-family: "Open Sans", sans-serif; font-weight: 700; fill: var(--paper); letter-spacing: 1px; }
  .script { font-family: "Roboto Condensed", sans-serif; font-style: italic; font-weight: 300; fill: var(--ink); }
  .script-accent { font-weight: 700; fill: var(--red); }
  .banner-text { font-family: "Roboto Condensed", sans-serif; font-style: italic; font-weight: 300; fill: var(--paper); }

  .photo { position: absolute; }
  .photo--round { border-radius: 50%; border: 4px solid #e9e9e9; }

  .body-copy { position: absolute; left: 35px; width: 614px; font-size: 10.2px; line-height: 1.3; color: var(--ink); }

  .contact { position: absolute; text-align: center; font-size: 12.5px; line-height: 1.32; color: var(--ink); }
  .contact .name { font-weight: 700; font-size: 21px; color: var(--red); letter-spacing: 0.3px; line-height: 1.2; }
  .flyer--whitening .contact .name { color: var(--deep-red); font-size: 22px; }

  .brand { position: absolute; left: 368px; top: 30px; width: 185px; text-align: center; }
  .brand-name { font-weight: 800; font-size: 20px; color: var(--deep-red); letter-spacing: 2px; line-height: 1.1; }
  .brand-tag { font-weight: 700; font-size: 9px; line-height: 1.15; color: var(--ink); margin-top: 3px; }

  .offer { position: absolute; left: 300px; top: 216px; }
  .offer h2 { font-weight: 700; font-size: 22px; color: var(--deep-red); line-height: 1.2; white-space: nowrap; }
  .offer p { font-size: 16px; line-height: 1.32; white-space: nowrap; }
</style>
</head>
<body>
<div class="canvas">

  <!-- Laser lipo side -->
  <section class="flyer flyer--lipo">
    <div class="wash"></div>

    <div class="photo photo--round" style="left:315px;top:24px;width:120px;height:120px;background:radial-gradient(circle at 50% 45%,#f2ddd0,#d8b9a6);" role="img" aria-label="Photo of hips in white underwear"></div>
    <div class="photo photo--round" style="left:500px;top:22px;width:124px;height:124px;background:radial-gradient(circle at 50% 45%,#d9ab8c,#a8775a);" role="img" aria-label="Photo of a toned male torso"></div>
    <div class="photo photo--round" style="left:378px;top:12px;width:154px;height:154px;background:radial-gradient(circle at 50% 45%,#e6c0a4,#c49677);" role="img" aria-label="Photo of a waist with a measuring tape"></div>

    <div class="body-copy" style="top:176px;">This new innovative laser technology will break down the fat cells and promote the triglyceride in the cells overflow. The fat cells are significantly reduced, achieving weight loss immediately. At the same time, the outflow of the glycerol and free acids are decomposed in part by capillaries and lymphatic microtubule, partly transformed into energy by movement, and partly excreted by the kidneys.</div>
    <div class="body-copy" style="top:242px;">The velvetwave laser lipo can reduce from 2-15cm of body fat after a single treatment. The procedure is fast, relaxing and effective on any body parts without causing any side effects to the client.</div>

    <div class="photo" style="left:32px;top:300px;width:208px;height:115px;border:3px solid #fff;box-shadow:0 0 0 1px #ccc;background:linear-gradient(90deg,#c99a7d,#e0bca2 50%,#c99a7d);" role="img" aria-label="Before and after photo of a stomach"></div>

    <svg class="art" width="666" height="470" viewBox="0 0 666 470">
      <path d="M0 0 H268 C282 84 210 146 0 176 Z" fill="var(--shadow-black)"/>
      <path d="M0 0 H270 C272 70 205 135 0 165 Z" fill="var(--red)"/>
      <text class="headline-text" font-size="16" x="22" y="76" textLength="206" lengthAdjust="spacingAndGlyphs" transform="rotate(-15.4 22 76)">A non-invasive treatment that every</text>
      <text class="headline-text" font-size="16" x="30" y="97" textLength="200" lengthAdjust="spacingAndGlyphs" transform="rotate(-15.4 30 97)">salon and spa must have! Say no to</text>
      <text class="headline-text" font-size="16" x="40" y="121" textLength="194" lengthAdjust="spacingAndGlyphs" transform="rotate(-15.4 40 121)">Liposuction, surgery or crash diet.</text>
      <text class="headline-phone" font-size="22" x="63" y="147" textLength="152" lengthAdjust="spacingAndGlyphs" transform="rotate(-17 63 147)">01632960418</text>

      <text class="script" font-size="18" x="275" y="310" textLength="350" lengthAdjust="spacingAndGlyphs">cost is £40 per session or full course of 8 sessions at £199</text>

      <path d="M244 332.5 L258 317 H666 V348 H258 Z" fill="var(--banner-red)"/>
      <text class="banner-text" font-size="16" x="275" y="338" textLength="368" lengthAdjust="spacingAndGlyphs">gift certificates perfect for birthdays, christmas or just the one you love.</text>

      <text class="script" font-size="16" x="275" y="365" textLength="147" lengthAdjust="spacingAndGlyphs">also a voucher with an extra</text>
      <text class="script script-accent" font-size="19" x="426" y="365" textLength="57" lengthAdjust="spacingAndGlyphs">10% off</text>
    </svg>

    <div class="contact" style="left:345px;top:383px;width:320px;">
      <div class="name">REBECCA DOWD</div>
      <div>number 01632960418</div>
      <div>address 27 heol y felin pentwyn cf145qt</div>
      <div>email dowdkevindowd@mailbox-example.co.uk</div>
    </div>
  </section>

  <!-- Teeth whitening side -->
  <section class="flyer flyer--whitening">
    <div class="wash"></div>

    <div class="photo" style="left:0;top:172px;width:365px;height:326px;background:radial-gradient(ellipse at 45% 45%,#f1e6dc 0%,#dcc7b6 45%,#ece7e2 80%);" role="img" aria-label="Photo of a smiling family lying on the floor"></div>

    <div class="brand">
      <div class="brand-name">VELVETWAVE</div>
      <div class="brand-tag">The fastest growing International<br>Beauty &amp; Aesthetic Brand...</div>
    </div>
    <div class="photo" style="left:555px;top:16px;width:90px;height:78px;border-radius:40%;background:radial-gradient(circle at 50% 50%,#d62a2a,#f3e9e9 75%,#fff);" role="img" aria-label="Illustration of a fruit splash"></div>

    <div class="photo" style="left:358px;top:92px;width:165px;height:113px;background:linear-gradient(90deg,#e9a48f,#f0dcd0 50%,#e9a48f);" role="img" aria-label="Before and after photo of a smile"></div>
    <div class="photo" style="left:545px;top:103px;width:82px;height:44px;background:linear-gradient(#b9443f,#e7d4b8 50%,#b9443f);" role="img" aria-label="Close-up of teeth before whitening"></div>
    <div class="photo" style="left:545px;top:150px;width:82px;height:40px;background:linear-gradient(#b9443f,#f4efe9 50%,#b9443f);" role="img" aria-label="Close-up of teeth after whitening"></div>

    <div class="offer">
      <h2>We offer two different treatments…</h2>
      <p><b>20 minute</b> express £30 each or 2 people for £50<br><b>45 minute</b> premium (longer lasting) £50 each or<br>2 people for £80</p>
    </div>

    <svg class="art" width="730" height="497" viewBox="0 0 730 497">
      <path d="M0 0 H280 C300 92 225 156 0 182 Z" fill="var(--shadow-black)"/>
      <path d="M0 0 H284 C290 80 222 145 0 172 Z" fill="var(--red)"/>
      <text class="headline-text" font-size="18" x="22" y="80" textLength="218" lengthAdjust="spacingAndGlyphs" transform="rotate(-16.4 22 80)">We use a non peroxide gel so no</text>
      <text class="headline-text" font-size="18" x="30" y="106" textLength="216" lengthAdjust="spacingAndGlyphs" transform="rotate(-16.4 30 106)">sensitivity at all and completely</text>
      <text class="headline-text" font-size="18" x="32" y="136" textLength="228" lengthAdjust="spacingAndGlyphs" transform="rotate(-16.4 32 136)"><tspan font-size="26" font-style="italic">pain free</tspan> cosmetic procedure.</text>
      <text class="headline-phone" font-size="23" x="67" y="156" textLength="160" lengthAdjust="spacingAndGlyphs" transform="rotate(-18 67 156)">01632960418</text>

      <path d="M282 328.5 L296 312 H730 V345 H296 Z" fill="var(--banner-red)"/>
      <text class="banner-text" font-size="16" x="306" y="334" textLength="373" lengthAdjust="spacingAndGlyphs">gift certificates perfect for birthdays christmas or just the one you love</text>

      <text class="script" font-size="16.5" x="371" y="370" textLength="303" lengthAdjust="spacingAndGlyphs">bring the voucher and claim a <tspan class="script-accent" font-size="18">free top up pen</tspan> or</text>
      <text class="script" font-size="16.5" x="452" y="392" textLength="141" lengthAdjust="spacingAndGlyphs">have an extra <tspan class="script-accent" font-size="18">10% off</tspan></text>
    </svg>

    <div class="contact" style="left:373px;top:405px;width:320px;">
      <div class="name">REBECCA DOWD</div>
      <div>number 01632960418</div>
      <div>address 27 heol y felin pentwyn cf145qt</div>
      <div>email dowdkevindowd@mailbox-example.co.uk</div>
    </div>
  </section>

</div>
</body>
</html>
```